Retractable Banner Design for Retail Shopping Event

I need a design for a 33” by 86” retractable banner. It should have my logo at the top (the largest element of the design) and the banner should also include my website and Instagram handle:
www.verikamode.com
@verikamode
I have included product pictures in the brief that can be used. I also included different versions of my logo file, including AI. I need the file to be ready to upload to my printer.
My store is an upscale women’s boutique. I am also attaching designs I have selected in the past to give an idea of my aesthetic.

```html
<!DOCTYPE html>
<html lang="en">
<head>
<meta charset="utf-8">
<title>Verika Mode — Retractable Banner</title>
<link href="https://fonts.googleapis.com/css2?family=Abril+Fatface&family=Pinyon+Script&family=Josefin+Sans:wght@700&display=swap" rel="stylesheet">
<style>
  :root {
    --blush: #ecd3d0;
    --slate: #656a6a;
    --clay: #b0836f;
    --panel-top: #ffffff;
    --panel-bottom: #e6e2ea;
  }
  html, body { margin: 0; padding: 0; overflow: hidden; }
  body { width: 1200px; height: 3127px; background: var(--blush); }
  .banner { position: relative; width: 1200px; height: 3127px; background: var(--blush); overflow: hidden; }

  .brand-frame {
    position: absolute; left: 159px; top: 141px; width: 882px; height: 306px;
    border: 4px solid var(--slate); border-bottom: none; box-sizing: border-box;
  }
  .brand-rule { position: absolute; top: 443px; height: 4px; background: var(--slate); }
  .brand-rule.left { left: 159px; width: 363px; }
  .brand-rule.right { left: 675px; width: 366px; }
  .brand-name {
    position: absolute; left: 159px; width: 882px; top: 205px; margin: 0;
    text-align: center; font-family: "Abril Fatface", serif; font-weight: 400;
    font-size: 160px; line-height: 1; letter-spacing: 4px; color: var(--slate);
  }
  .brand-sub {
    position: absolute; left: 522px; width: 153px; top: 420px;
    text-align: center; font-family: "Abril Fatface", serif; font-weight: 400;
    font-size: 44px; line-height: 1; letter-spacing: 3px; color: var(--slate);
  }

  .tagline {
    position: absolute; left: 182px; top: 1607px; width: 1800px;
    transform: translate(-50%, -50%) rotate(-90deg);
    text-align: center; font-family: "Pinyon Script", cursive;
    font-size: 150px; line-height: 1; letter-spacing: 14px; color: var(--clay);
    white-space: nowrap;
  }

  .product-stand {
    position: absolute; left: 415px; width: 699px; height: 290px;
    border: 17px solid var(--clay); box-sizing: border-box;
    background: linear-gradient(var(--panel-top), var(--panel-bottom));
  }
  .stand-1 { top: 665px; }
  .stand-2 { top: 1187px; }
  .stand-3 { top: 1735px; }
  .stand-4 { top: 2259px; }

  .product { position: absolute; }
  .product-slippers { left: 510px; top: 510px; width: 473px; height: 376px; border-radius: 40% 45% 30% 30%;
    background: linear-gradient(160deg, #f0d8cc, #a28d9e); }
  .product-tote { left: 580px; top: 992px; width: 369px; height: 428px; border-radius: 8px;
    background: linear-gradient(180deg, #e6cbbd, #d2b3a5); }
  .product-earrings { left: 491px; top: 1680px; width: 552px; height: 249px; border-radius: 30px;
    background: radial-gradient(circle at 30% 50%, #e2b84a, rgba(226,184,74,0) 60%),
                radial-gradient(circle at 72% 50%, #e2b84a, rgba(226,184,74,0) 60%); }
  .product-tray { left: 534px; top: 2147px; width: 473px; height: 353px; border-radius: 50%;
    background: radial-gradient(ellipse, #d9bd8a, #7a6448); }

  .contact-frame {
    position: absolute; left: 159px; top: 2716px; width: 882px; height: 305px;
    border: 4px solid var(--slate); box-sizing: border-box;
  }
  .contact-web, .contact-social {
    position: absolute; font-family: "Josefin Sans", sans-serif; font-weight: 700;
    color: var(--slate); line-height: 1; margin: 0;
  }
  .contact-web { left: 159px; width: 882px; top: 2810px; text-align: center; font-size: 54px; }
  .contact-social { left: 404px; top: 2880px; font-size: 54px; display: flex; align-items: center; gap: 14px; }
  .social-dot { width: 50px; height: 50px; border-radius: 50%; background: var(--slate); }
</style>
</head>
<body>
<main class="banner">
  <header>
    <div class="brand-frame"></div>
    <div class="brand-rule left"></div>
    <div class="brand-rule right"></div>
    <h1 class="brand-name">VERIKA</h1>
    <div class="brand-sub">MODE</div>
  </header>

  <div class="tagline">Make Your Life Beautiful</div>

  <section class="products">
    <div class="product-stand stand-1"></div>
    <div class="product product-slippers" role="img" aria-label="Product photo: blush pom-pom slide slippers"></div>
    <div class="product-stand stand-2"></div>
    <div class="product product-tote" role="img" aria-label="Product photo: nude tote bag with blue snake print"></div>
    <div class="product-stand stand-3"></div>
    <div class="product product-earrings" role="img" aria-label="Product photo: gold beaded clover earrings with crystals"></div>
    <div class="product-stand stand-4"></div>
    <div class="product product-tray" role="img" aria-label="Product photo: round leopard print serving tray"></div>
  </section>

  <footer>
    <div class="contact-frame"></div>
    <p class="contact-web">www.verikamode.com</p>
    <p class="contact-social"><span class="social-dot"></span>verikamode</p>
  </footer>
</main>
</body>
</html>
```